Mosvane Design

Looking for Mosvane banner and square design:
Mosvane Banner
W:1600 px H:400 px
Square
120x120

Logo attached.

Description: Data-Driven stock market portfolio management using quantitative analysis.

```html
<!DOCTYPE html>
<html lang="en">
<head>
<meta charset="utf-8">
<title>Mosvane Banner</title>
<link rel="stylesheet" href="https://fonts.googleapis.com/css2?family=Outfit:wght@300;600&display=swap">
<style>
  :root {
    --bg-light: #f7f8f9;
    --bg-shade: #eceef0;
    --brand-blue: #0a73ba;
    --brand-navy: #165786;
    --title-blue: #1b6fb3;
    --logo-blue: #1d5f8f;
    --white: #ffffff;
    --outline: #2b2b2b;
  }
  html, body {
    margin: 0;
    padding: 0;
    overflow: hidden;
    background: var(--white);
  }
  .banner {
    position: relative;
    width: 1200px;
    height: 300px;
    overflow: hidden;
    background: linear-gradient(120deg, var(--bg-light) 0%, var(--bg-shade) 45%, var(--bg-light) 100%);
    font-family: "Outfit", sans-serif;
  }
  .banner__art {
    position: absolute;
    inset: 0;
    width: 1200px;
    height: 300px;
  }
  .brand {
    position: absolute;
    left: 47px;
    top: 58px;
    display: flex;
    align-items: center;
    gap: 12px;
  }
  .brand__dot {
    width: 34px;
    height: 34px;
    border-radius: 50%;
    background: var(--brand-blue);
  }
  .brand__name {
    font-weight: 600;
    font-size: 30px;
    letter-spacing: 0.5px;
    color: var(--logo-blue);
  }
  .headline {
    position: absolute;
    left: 47px;
    top: 168px;
    margin: 0;
    font-weight: 300;
    font-size: 30px;
    line-height: 42px;
    color: var(--title-blue);
    letter-spacing: 0.2px;
  }
</style>
</head>
<body>
<div class="banner">
  <svg class="banner__art" viewBox="0 0 1600 400" xmlns="http://www.w3.org/2000/svg">
    <defs>
      <linearGradient id="dashboardTone" x1="0" y1="0" x2="1" y2="1">
        <stop offset="0" stop-color="#f4f7fa"/>
        <stop offset="1" stop-color="#dce6ef"/>
      </linearGradient>
      <linearGradient id="officeTone" x1="0" y1="0" x2="1" y2="1">
        <stop offset="0" stop-color="#c9d6df"/>
        <stop offset="0.6" stop-color="#8fa3b1"/>
        <stop offset="1" stop-color="#5e6b73"/>
      </linearGradient>
    </defs>

    <!-- faint background facets -->
    <polygon class="facet" points="0,0 420,0 260,400 0,400" fill="#ffffff" opacity="0.35"/>
    <polygon class="facet" points="620,0 980,0 860,400 520,400" fill="#ffffff" opacity="0.3"/>

    <!-- top-right stripes -->
    <polygon class="stripe stripe--blue" points="1320,0 1385,0 1535,155 1440,155" fill="var(--brand-blue)"/>
    <polygon class="stripe stripe--navy" points="1425,0 1600,0 1600,228" fill="var(--brand-navy)"/>

    <!-- navy sweep behind dashboard -->
    <line class="sweep" x1="1115" y1="238" x2="1430" y2="560" stroke="var(--brand-navy)" stroke-width="300" stroke-linecap="round"/>

    <!-- blue sweep behind team photo -->
    <line class="sweep sweep--blue" x1="1475" y1="275" x2="1640" y2="440" stroke="var(--brand-blue)" stroke-width="194" stroke-linecap="round"/>

    <!-- dashboard circle -->
    <circle cx="1115" cy="240" r="120" fill="var(--white)"/>
    <circle cx="1115" cy="240" r="113" fill="url(#dashboardTone)" role="img" aria-label="Portfolio analytics dashboard with bar charts and tables"/>

    <!-- team photo circle -->
    <circle cx="1475" cy="277" r="84" fill="url(#officeTone)" role="img" aria-label="Team of analysts reviewing portfolio charts on a laptop"/>

    <!-- accent circles -->
    <circle cx="967" cy="170" r="58" fill="var(--brand-blue)"/>
    <circle cx="1267" cy="75" r="29" fill="var(--brand-blue)"/>

    <!-- outlined cross marks -->
    <g class="crosses" fill="none" stroke="var(--outline)" stroke-width="1">
      <g transform="translate(1070,25)">
        <path d="M0,6 L6,0 L21,15 L36,0 L42,6 L27,21 L42,36 L36,42 L21,27 L6,42 L0,36 L15,21 Z"/>
        <path transform="translate(50,0)" d="M0,6 L6,0 L21,15 L36,0 L42,6 L27,21 L42,36 L36,42 L21,27 L6,42 L0,36 L15,21 Z"/>
      </g>
      <g transform="translate(655,137) scale(0.72)">
        <path d="M0,6 L6,0 L21,15 L36,0 L42,6 L27,21 L42,36 L36,42 L21,27 L6,42 L0,36 L15,21 Z"/>
        <path transform="translate(50,0)" d="M0,6 L6,0 L21,15 L36,0 L42,6 L27,21 L42,36 L36,42 L21,27 L6,42 L0,36 L15,21 Z"/>
      </g>
    </g>
  </svg>

  <div class="brand">
    <span class="brand__dot"></span>
    <span class="brand__name">Mosvane</span>
  </div>

  <h1 class="headline">Data-Driven Stock Market Portfolio<br>Management Using Quantitative Analysis</h1>
</div>
</body>
</html>
```